Brindlow Legal Business Card

I require a corporate business card for a new legal services business.

I do not have a logo, nor do I want one.

I require a clean, neat a professional card for a law firm.

Details:

Business Name: Brindlow Legal
Name: Delia ter Hulst
Title: Corporate Services Manager
Location: Office 14 (Top Floor), Kelvara Business Centre, Dunmore Ash Street, Alotau CBD, Milne Bay Province.
Postal Address: PO Box 537, Alotau, 211, Milne Bay Province, Papua New Guinea.
Contact: T: +675 6428153, F: +675 6427602, M: +675 79154368, E: dterhulst@brindlowqx.com.pg.

I look forward to your design submissions.

Legal

```html
<!DOCTYPE html>
<html lang="en">
<head>
<meta charset="utf-8">
<title>Brindlow Legal — Business Card</title>
<link rel="stylesheet" href="https://fonts.googleapis.com/css2?family=Didact+Gothic&display=swap">
<style>
  :root {
    --navy: #213564;
    --navy-deep: #1b2c55;
    --grey: #8a8d93;
    --ink: #1f1f24;
    --paper: #ffffff;
    --backdrop: #e4e6ea;
  }
  * { box-sizing: border-box; margin: 0; padding: 0; }
  html, body { width: 1200px; height: 680px; overflow: hidden; }
  body {
    background: var(--backdrop);
    font-family: "Didact Gothic", "Century Gothic", sans-serif;
    position: relative;
  }
  .card {
    position: absolute;
    top: 186px;
    width: 540px;
    height: 308px;
    border-radius: 16px;
    overflow: hidden;
    box-shadow: 0 6px 18px rgba(20, 30, 60, 0.18);
  }
  .card--back { left: 40px; background: var(--navy); }
  .card--front { left: 620px; background: var(--paper); }

  /* back */
  .back-name {
    position: absolute;
    left: 0; right: 0; top: 96px;
    text-align: center;
    font-size: 56px;
    color: #c9ccd2;
    letter-spacing: 0.5px;
  }
  .email-tab {
    position: absolute;
    right: 0; bottom: 0;
    width: 290px; height: 44px;
  }
  .email-tab svg { position: absolute; inset: 0; }
  .email-tab span {
    position: absolute;
    right: 22px; bottom: 12px;
    font-size: 14px;
    letter-spacing: 0.3px;
  }
  .card--back .email-tab span { color: var(--navy); }
  .card--front .email-tab span { color: var(--paper); }

  /* front */
  .firm-name {
    position: absolute;
    left: 34px; top: 44px;
    font-size: 36px;
    color: var(--navy);
    letter-spacing: 0.3px;
  }
  .divider {
    position: absolute;
    left: 34px; right: 34px; top: 98px;
    height: 1.5px;
    background: var(--navy);
  }
  .person {
    position: absolute;
    right: 34px; top: 66px;
    text-align: right;
  }
  .person-name { font-size: 21px; color: var(--ink); line-height: 1; }
  .person-title {
    margin-top: 10px;
    font-size: 14.5px;
    color: var(--navy);
    letter-spacing: 0.2px;
  }
  .address-block {
    position: absolute;
    left: 34px;
    font-size: 14.5px;
    line-height: 1.22;
    color: var(--ink);
  }
  .address-block .label { color: var(--navy); }
  .address-block--postal { top: 108px; }
  .address-block--location { top: 214px; }
  .rule-short {
    position: absolute;
    left: 34px; top: 204px;
    width: 200px; height: 1px;
    background: var(--grey);
  }
  .contact-list {
    position: absolute;
    right: 34px; top: 134px;
    list-style: none;
    font-size: 13.5px;
    line-height: 1.35;
    color: var(--ink);
    text-align: right;
  }
  .contact-list li { display: flex; align-items: center; justify-content: flex-end; gap: 6px; }
  .contact-list svg { width: 12px; height: 12px; flex: none; }
</style>
</head>
<body>

  <section class="card card--back" aria-label="Business card, reverse side">
    <div class="back-name">Brindlow Legal</div>
    <div class="email-tab">
      <svg viewBox="0 0 290 44" preserveAspectRatio="none" aria-hidden="true">
        <path d="M0 44 C6 14 18 0 44 0 H290 V44 Z" fill="var(--paper)"/>
      </svg>
      <span>dterhulst@brindlowqx.com.pg</span>
    </div>
  </section>

  <section class="card card--front" aria-label="Business card, front side">
    <div class="firm-name">Brindlow Legal</div>

    <div class="person">
      <div class="person-name">Delia ter Hulst</div>
    </div>
    <div class="divider"></div>
    <div class="person" style="top:100px">
      <div class="person-title" style="margin-top:0">Corporate Services Manager</div>
    </div>

    <div class="address-block address-block--postal">
      <div class="label">Postal Address:</div>
      <div>PO Box 537, Alotau, 211</div>
      <div>Milne Bay Province</div>
      <div>Papua New Guinea</div>
    </div>

    <div class="rule-short"></div>

    <div class="address-block address-block--location">
      <div><span class="label">Location:</span> Office 14 (Top Floor)</div>
      <div>Kelvara Business Centre</div>
      <div>Dunmore Ash Street</div>
      <div>Alotau CBD, Milne Bay Province</div>
    </div>

    <ul class="contact-list">
      <li>+675 6428153
        <svg viewBox="0 0 12 12" aria-label="Telephone"><circle cx="6" cy="6" r="5.3" fill="none" stroke="var(--ink)" stroke-width="1"/><path d="M3.8 3.2c.5-.4 1-.3 1.2.2l.4.9c.1.3 0 .6-.3.8l-.3.2c.3.8.9 1.4 1.6 1.7l.2-.3c.2-.3.5-.4.8-.3l.9.4c.5.2.6.7.2 1.2-.5.6-1.3.7-2 .3C5 7.6 4 6.5 3.5 5.2c-.3-.8-.2-1.5.3-2z" fill="var(--ink)"/></svg>
      </li>
      <li>+675 6427602
        <svg viewBox="0 0 12 12" aria-label="Fax"><rect x="3" y="1" width="6" height="4" fill="none" stroke="var(--ink)" stroke-width="1"/><rect x="1" y="5" width="10" height="6" rx="1" fill="var(--ink)"/><rect x="3" y="7" width="6" height="1" fill="var(--paper)"/></svg>
      </li>
      <li>+675 79154368
        <svg viewBox="0 0 12 12" aria-label="Mobile"><rect x="3" y="0.5" width="6" height="11" rx="1" fill="var(--ink)"/><rect x="4" y="2" width="4" height="4" fill="var(--paper)"/></svg>
      </li>
    </ul>

    <div class="email-tab">
      <svg viewBox="0 0 290 44" preserveAspectRatio="none" aria-hidden="true">
        <path d="M0 44 C6 14 18 0 44 0 H290 V44 Z" fill="var(--navy)"/>
      </svg>
      <span>dterhulst@brindlowqx.com.pg</span>
    </div>
  </section>

</body>
</html>
```